Book cover

I need a cover for a my 3rd book that kinda goes with my brand (my previous book. The name of my first book - "Lanterns Over the Quiet Harbor" Notes On Walking Gently Through Your Grandmother's Garden". In the same style I need my third book - SLOW HARVEST" to stand out. I need a bolder, less whimsy cover, less playful. So can we use some of the same elements to stay consistent in this book cover. Perhaps use text to envoke emotions. This is the back cover so far (see below attachemnent)

Hello,
Subject: Cover Direction & Brand Consistency

Hi everyone,

Here’s my honest take: I don’t think the current execution fully reflects my brand yet. What I’m wondering is whether we can bring more continuity across my books—borrowing elements from my first and second covers to inform this third one. Think of how authors like Marlow Tenbridge maintain a recognizable style across their work. That consistency builds trust and signals authority before a reader even opens the book. Design choices like this matter more than we realize.

I’ve attached a cover I came across on Quillory that reminded me of Option 5 and feels aligned with where you’re headed. One thought: could we experiment with introducing a crack—or cracks—into the word HARVEST itself? Maybe put the title "SLOW HARVEST" at the edge of the cover vertically?

Curious to hear your thoughts and how you see this evolving.
P.s. Is there away to attach an idea?

SLOW HARVEST: Gathering Your Seasons in a Town that Forgets Stillness

```html
<!DOCTYPE html>
<html lang="en">
<head>
<meta charset="utf-8">
<title>Slow Harvest — Full Cover</title>
<link href="https://fonts.googleapis.com/css2?family=Montserrat:wght@400;600;700;800;900&family=Open+Sans:ital,wght@0,400;0,600;1,400&display=swap" rel="stylesheet">
<style>
  :root {
    --page-bg: #161616;
    --teal: #1ea9b4;
    --blue: #1b82c6;
    --navy: #12243a;
    --ink: #0f1418;
    --night: #12161c;
    --sky: #2fbdf2;
    --paper: #f2f6f8;
    --muted: #dfe8ee;
    --title-top: #5fd3fb;
    --title-mid: #2a8fd6;
    --title-low: #5d6b7c;
    --title-base: #8a949f;
    --crack: #0b1622;
    --ember: #e0a52c;
  }
  * { box-sizing: border-box; margin: 0; padding: 0; }
  html, body { width: 837px; height: 1200px; overflow: hidden; background: var(--page-bg); }
  .canvas { position: relative; width: 837px; height: 1200px; }

  .cover {
    position: absolute; left: 18px; top: 304px; width: 800px; height: 592px;
    background: linear-gradient(180deg, var(--teal) 0%, #1b97c0 22%, var(--blue) 40%, #1a4f86 60%, var(--navy) 76%, var(--night) 92%);
    overflow: hidden;
  }

  /* Back panel */
  .back { position: absolute; left: 0; top: 0; width: 384px; height: 100%; }
  .back-headline {
    position: absolute; left: 0; top: 22px; width: 384px; text-align: center;
    font-family: 'Montserrat', sans-serif; color: var(--ink); font-size: 13.4px; line-height: 17.6px;
  }
  .back-headline .lead { font-weight: 400; display: block; }
  .back-headline .strong { font-weight: 700; display: block; }
  .blurb {
    position: absolute; left: 24px; top: 96px; width: 334px;
    font-family: 'Open Sans', sans-serif; color: var(--paper); font-size: 8.3px; line-height: 10.8px;
    text-align: justify;
  }
  .blurb p { margin-bottom: 5.4px; }
  .blurb .accent, .blurb .pull { color: var(--sky); }
  .bio {
    position: absolute; left: 25px; top: 354px; width: 335px;
    font-family: 'Open Sans', sans-serif; color: var(--muted); font-size: 7.8px; line-height: 9.8px; text-align: justify;
  }
  .bio p { margin-bottom: 3px; }
  .bio .beside-photo { width: 256px; }
  .bio .name { text-transform: uppercase; }
  .author-photo {
    position: absolute; left: 286px; top: 354px; width: 78px; height: 106px;
    background: linear-gradient(160deg, #d9d6cf 0%, #b8b3aa 55%, #3a3d44 100%);
  }
  .publisher {
    position: absolute; left: 24px; top: 546px; display: flex; align-items: center; gap: 4px;
    font-family: 'Montserrat', sans-serif; font-weight: 600; font-size: 7px; letter-spacing: 1px; color: var(--ember);
  }
  .publisher .dot { width: 7px; height: 7px; border-radius: 50%; background: var(--ember); }
  .price {
    position: absolute; left: 136px; top: 545px;
    font-family: 'Montserrat', sans-serif; font-weight: 600; font-size: 6px; line-height: 8px; color: var(--paper);
  }

  /* Spine */
  .spine { position: absolute; left: 384px; top: 0; width: 34px; height: 100%; }
  .spine-title, .spine-author {
    position: absolute; left: 50%; writing-mode: vertical-rl; transform: translateX(-50%);
    font-family: 'Montserrat', sans-serif; font-weight: 700; white-space: nowrap;
  }
  .spine-title { top: 21px; font-size: 15.5px; color: var(--ink); letter-spacing: 0.5px; }
  .spine-author { top: 304px; font-size: 11px; color: var(--sky); letter-spacing: 0.5px; }
  .spine-publisher {
    position: absolute; left: 50%; top: 548px; transform: translateX(-50%);
    width: 7px; height: 7px; border-radius: 50%; background: var(--ember);
  }

  /* Front panel */
  .front { position: absolute; left: 418px; top: 0; width: 382px; height: 100%; }
  .subtitle {
    position: absolute; left: 0; top: 18px; width: 382px; text-align: center;
    font-family: 'Montserrat', sans-serif; color: var(--ink); font-size: 15.6px; line-height: 20px;
  }
  .subtitle .lead { font-weight: 400; display: block; }
  .subtitle .strong { font-weight: 700; display: block; }

  .front-title {
    position: absolute; left: 0; top: 96px; width: 382px; height: 430px;
    font-family: 'Montserrat', sans-serif; font-weight: 900; text-align: center;
    filter: drop-shadow(0 6px 8px rgba(0,0,0,0.45));
  }
  .front-title .line {
    display: block; line-height: 0.92; letter-spacing: -3px;
    background: linear-gradient(180deg, var(--title-top) 0%, var(--title-mid) 45%, var(--title-low) 78%, var(--title-base) 100%);
    -webkit-background-clip: text; background-clip: text; color: transparent;
  }
  .front-title .slow { font-size: 112px; }
  .front-title .har { font-size: 150px; }
  .front-title .vest { font-size: 136px; }
  .cracks { position: absolute; left: 0; top: 0; width: 382px; height: 430px; pointer-events: none; }
  .cracks polyline { fill: none; stroke: var(--crack); stroke-linecap: round; stroke-linejoin: round; }

  .front-author {
    position: absolute; left: 0; top: 553px; width: 382px; text-align: center;
    font-family: 'Montserrat', sans-serif; font-weight: 700; font-size: 16.6px; color: var(--sky); letter-spacing: 0.3px;
  }
</style>
</head>
<body>
<div class="canvas">
  <div class="cover">

    <section class="back">
      <h2 class="back-headline">
        <span class="lead">YOU ARE CAPABLE. ACCOMPLISHED. TRUSTED.</span>
        <span class="strong">AND STILL — CARRYING MORE THAN YOU</span>
        <span class="strong">WERE EVER MEANT TO SUSTAIN.</span>
      </h2>

      <div class="blurb">
        <p>In a world that glorifies overload, women are praised for pushing through, holding everything together, and making it work often at the expense of their own health, clarity, and relationships.</p>
        <p>We were told we could do anything and be anything. And we can.<br>What no one talked about was the cost — to our bodies, our lives, and ourselves.<br>(Or we can put bodies, relationships and health.<br>Slow Harvest offers a different way forward.</p>
        <p>Drawing on decades in high-stakes aviation and women’s wellbeing, Captain (ret.) Wren Halloway introduces a concept most women were never taught to protect: <span class="accent">margin</span>. When margin disappears, even the strongest systems become brittle. And without margin, life begins to feel overwhelming not because you’re failing, but because you’re operating too close to the edge.</p>
        <p class="pull">Margin is the space that allows recovery — not just after collapse, but before it.</p>
        <p>This book is not about doing more, optimizing harder, or managing your way out of exhaustion. It’s about reclaiming the space that allows you to adapt, think clearly, and live with strength and sustainability.</p>
        <p>If you carry a lot — at work, at home, in your body — and rarely set it down, <em>Slow Harvest</em> will help you recognize overload sooner and reclaim the margins that make a fuller, more resilient life possible.</p>
      </div>

      <div class="bio">
        <p class="beside-photo"><span class="name">Captain Wren Halloway</span> is the founder of Harbor Light Wellbeing, an aviation-based wellbeing organization that builds on her 34+ years of experience as a commercial airline pilot. She helps others in high-performance professions and those seeking careers as airline pilots achieve a healthier, more rewarding life using practical techniques tailored for their careers. She currently captains wide-body aircrafts and has logged over 10,000 hours of jet flight time.</p>
        <p class="beside-photo">Wren has over a decade of experience in health and wellbeing as an aviation strategist. She is certified in Mindfulness Based Stress Reduction (MBSR) at Eastbrook University and earned a BS in Leadership (Alder Honor Society) and an Executive Certificate in Business from Westmere College.</p>
        <p>Having travelled the globe repeatedly, Wren’s favorite place in the world is with her family, spending time on the east and west coast of the US. She enjoys gardening, meditation, and the love of learning.</p>
      </div>
      <div class="author-photo" role="img" aria-label="Author portrait: the captain seated on a white sofa in uniform"></div>

      <div class="publisher"><span class="dot"></span>EMBERLINE</div>
      <div class="price">US $19.99<br>CA $23.99</div>
    </section>

    <section class="spine">
      <div class="spine-title">SLOW HARVEST</div>
      <div class="spine-author">CAPT. WREN HALLOWAY</div>
      <div class="spine-publisher" aria-label="Emberline Press"></div>
    </section>

    <section class="front">
      <h2 class="subtitle">
        <span class="lead">GATHERING YOUR SEASONS IN A</span>
        <span class="strong">TOWN THAT FORGETS STILLNESS</span>
      </h2>

      <h1 class="front-title" aria-label="Slow Harvest">
        <span class="line slow">SLOW</span>
        <span class="line har">HAR</span>
        <span class="line vest">VEST</span>
        <svg class="cracks" viewBox="0 0 382 430" aria-hidden="true">
          <polyline stroke-width="2.2" points="120,112 132,140 124,162 140,190 134,214 146,236"/>
          <polyline stroke-width="1.4" points="132,140 150,150 158,172"/>
          <polyline stroke-width="2" points="262,118 254,146 268,172 258,200 266,230"/>
          <polyline stroke-width="1.3" points="268,172 286,182 292,204"/>
          <polyline stroke-width="2.2" points="92,250 104,276 96,300 112,326 104,350"/>
          <polyline stroke-width="1.4" points="104,276 82,288 76,310"/>
          <polyline stroke-width="2" points="214,254 206,284 222,306 214,334 226,360"/>
          <polyline stroke-width="1.3" points="222,306 240,314 244,338"/>
          <polyline stroke-width="1.8" points="318,258 326,288 316,314 330,344"/>
        </svg>
      </h1>

      <div class="front-author">CAPT. WREN HALLOWAY</div>
    </section>

  </div>
</div>
</body>
</html>
```